Admin Backend Redesign

We need a redesign for our backend which supoosed to make the backoffice look more modern!

I will add screenshots of the backoffice so you know what data will be shown in the Admin.

Have in mind that the users of this backend are Doctors. We need a clinical look, modern and sharp. The backoffice is responsive, have that in mind. We need the backoffice to look as professional as possible.

The theme used for the website is: http://velmora.brisk-sample.net/

ON the main page of the backoffice, under every widget i need some space to write an explanation what the widget is about.

The color code used in our logo and website is #57aad4 combined with white.

We are open for ideas!
Updates

Project Deadline Extended
Reason: Designs are ok, but nothing innovative. Please use more modern designs!

Project Deadline Extended
Reason: Havent recieved a perfect design yet. Please read instructions carefully! Thank you

Project Deadline Extended
Reason: Hey everybody, sorry for the delay. We will decide in 3 days. If anyone wants to add a Design, that would be great.

Target Market(s)

Doctors, therapists

Industry/Entity Type

It Professional

Font styles to use
Sans Serif

Requirements
Must have
• Must look uptodate, modern, like new back offices look nowadays

```html
<!DOCTYPE html>
<html lang="de">
<head>
<meta charset="utf-8">
<title>Dashboard</title>
<link rel="stylesheet" href="https://fonts.googleapis.com/css2?family=Roboto:ital,wght@0,300;0,400;0,500;0,700;1,400;1,700&family=Crimson+Text:ital@1&display=swap">
<style>
:root{
  --brand:#57aad4;
  --brand-dark:#4a9cc6;
  --page:#f0f0f0;
  --panel:#ffffff;
  --line:#dde3e7;
  --text:#4a4a4a;
  --muted:#8a8a8a;
  --info-bg:#f2f7fb;
  --info-line:#d5e5f0;
  --accent:#f39c12;
  --link:#e8731a;
  --row-hi:#eef6d6;
  --green:#8cc63f;
  --green-dark:#5fa118;
  --dark:#2b2b2b;
}
*{box-sizing:border-box;margin:0;padding:0}
html,body{width:780px;height:1200px;overflow:hidden}
body{position:relative;background:var(--page);font-family:"Roboto",Arial,sans-serif;color:var(--text)}

.topbar{position:absolute;left:0;top:0;width:780px;height:37px;background:#fafafa;border-bottom:1px solid #d9d9d9}
.company-name{position:absolute;left:18px;top:15px;font-size:7px;letter-spacing:2px;color:#b7b7b7;font-weight:500}
.nav{position:absolute;right:0;top:0;height:37px;display:flex}
.nav a{display:flex;align-items:center;gap:5px;padding:0 13px;height:37px;border-left:1px solid #e0e0e0;font-size:7.5px;font-weight:700;color:#333;text-decoration:none;text-transform:uppercase}
.nav a.active{color:var(--brand);background:#f3f6f8}
.nav a.menu{padding:0 12px}

.titlebar{position:absolute;left:0;top:37px;width:780px;height:56px;background:#fff;border-bottom:1px solid #e2e2e2}
.page-title{position:absolute;left:19px;top:18px;display:flex;align-items:center;gap:6px;font-size:18px;font-weight:400;color:var(--brand)}
.user{position:absolute;right:18px;top:10px;display:flex;align-items:center;gap:4px;font-size:7.5px;font-style:italic;font-weight:700;color:#333}
.avatar{width:37px;height:37px;border-radius:50%;background:radial-gradient(circle at 50% 40%,#e4c9b4,#9fb8c9 70%);border:2px solid #e8e8e8}
.user .name{color:var(--brand)}

.widget{position:absolute;width:362px;background:var(--panel);border:1px solid var(--line);display:flex;flex-direction:column}
.col-left{left:19px}
.col-right{left:399px;width:363px}
.widget-head{height:27px;background:var(--brand);position:relative;display:flex;align-items:center;padding-left:9px;color:#fff;font-size:9.5px;font-weight:700;text-transform:uppercase;flex:none}
.toggle{position:absolute;right:0;top:0;width:28px;height:27px;border-left:1px solid rgba(255,255,255,.35);display:flex;align-items:center;justify-content:center}
.widget-body{flex:1;position:relative}
.widget-info{height:37px;flex:none;background:var(--info-bg);border-top:1px solid var(--info-line);position:relative;display:flex;align-items:center;padding:0 10px 0 30px}
.widget-info::before{content:"";position:absolute;left:10px;top:-6px;width:10px;height:10px;background:var(--info-bg);border-left:1px solid var(--info-line);border-top:1px solid var(--info-line);transform:rotate(45deg)}
.widget-info .icon{position:absolute;left:11px;top:10px;font-family:"Crimson Text",Georgia,serif;font-style:italic;font-weight:700;font-size:16px;color:var(--brand)}
.widget-info p{font-family:"Crimson Text",Georgia,serif;font-style:italic;font-size:7.4px;line-height:9.5px;color:var(--brand)}

.tip{position:absolute;background:var(--dark);color:#fff;font-size:6.5px;font-weight:700;padding:3px 6px;border-radius:2px;white-space:nowrap}
.tip::after{content:"";position:absolute;left:50%;bottom:-3px;margin-left:-3px;border:3px solid transparent;border-bottom:0;border-top-color:var(--dark)}
.tip.light{background:#fff;color:#333;border:1px solid #999;font-weight:400;box-shadow:0 1px 2px rgba(0,0,0,.2)}
.tip.light::after{display:none}

.lead{position:absolute;left:10px;top:13px;display:flex;align-items:center;gap:5px;font-size:8.6px;color:#222}
.btn{background:var(--accent);color:#fff;font-size:7px;font-weight:700;padding:4px 9px;border-radius:2px;text-transform:uppercase}
.copy{position:absolute;left:10px;right:10px;top:38px;font-size:7.3px;line-height:12.2px;color:#555}

.legend{position:absolute;font-size:6px;color:#444}
.legend li{list-style:none;display:flex;align-items:center;gap:5px;height:12px}
.legend i{display:block;width:8px;height:8px}

.search{position:absolute;right:10px;top:13px;width:122px;height:18px;background:#f1f1f1;border-radius:2px}
.search svg{position:absolute;right:5px;top:5px}
.grid{position:absolute;left:10px;right:10px;top:44px;border-collapse:collapse;font-size:7.5px;width:342px}
.grid th{text-align:left;font-size:6.8px;font-weight:700;color:#333;text-transform:uppercase;height:13px;padding:0 6px;border-bottom:1px solid #bbb;position:relative}
.grid td{height:19px;padding:0 6px;border-bottom:1px solid #e6e6e6;color:#555}
.grid th+th,.grid td+td{border-left:1px solid #e3e3e3}
.grid tr.hi td{background:var(--row-hi)}
.grid tbody tr:last-child td{border-bottom:1px solid #bbb}
.sort{position:absolute;right:4px;top:3px;width:5px;height:8px}
.sort::before,.sort::after{content:"";position:absolute;left:0;border:2.5px solid transparent}
.sort::before{top:-2px;border-bottom-color:#aaa}
.sort::after{bottom:-2px;border-top-color:#aaa}
.link{color:var(--link)}
.link::before{content:"\203A";font-weight:700;margin-right:3px}
.stars{color:var(--green);letter-spacing:1px;font-size:8.5px}
.bar{width:60px;height:5px;background:#e8e8e8;border-radius:3px;position:relative}
.bar span{position:absolute;left:0;top:0;height:5px;border-radius:3px;background:linear-gradient(var(--green),var(--green-dark))}

.table-meta{position:absolute;left:0;right:0;top:167px;text-align:center;font-size:5.8px;font-style:italic;color:#777}
.pager{position:absolute;left:0;right:0;top:176px;display:flex;justify-content:center}
.pager span{width:12px;height:12px;border:1px solid #ccc;margin-left:-1px;font-size:6.3px;display:flex;align-items:center;justify-content:center;color:var(--link);background:#fff}
.pager span.current{color:#888;background:#f4f4f4}

.footer{position:absolute;left:0;top:1182px;width:780px;height:18px;border-top:1px solid #ddd;text-align:center;font-size:5.6px;color:#888;padding-top:6px}
</style>
</head>
<body>

<header class="topbar">
  <div class="company-name">COMPANY LOGO</div>
  <nav class="nav">
    <a class="active" href="#"><svg width="10" height="9" viewBox="0 0 10 9"><path d="M5 0 L10 4.5 H8.5 V9 H6 V6 H4 V9 H1.5 V4.5 H0 Z" fill="#57aad4"/></svg>Dashboard</a>
    <a href="#"><svg width="9" height="10" viewBox="0 0 9 10"><circle cx="4.5" cy="2.6" r="2.4" fill="#333"/><path d="M0 10 C0 5.5 9 5.5 9 10 Z" fill="#333"/></svg>Mein Konto</a>
    <a href="#"><svg width="11" height="11" viewBox="0 0 11 11"><rect x="0.6" y="1.6" width="7.5" height="8.8" fill="none" stroke="#333" stroke-width="1.2"/><path d="M2.5 4 H6 M2.5 6 H5" stroke="#333"/><path d="M5 7.5 L10 1.5 L11 2.5 L6 8.5 L4.6 8.9 Z" fill="#333"/></svg>Patientenbewertungen</a>
    <a class="menu" href="#"><svg width="11" height="9" viewBox="0 0 11 9"><path d="M0 1 H11 M0 4.5 H11 M0 8 H11" stroke="#333" stroke-width="1.6"/></svg></a>
  </nav>
</header>

<section class="titlebar">
  <h1 class="page-title"><svg width="15" height="13" viewBox="0 0 10 9"><path d="M5 0 L10 4.5 H8.5 V9 H6 V6 H4 V9 H1.5 V4.5 H0 Z" fill="#57aad4"/></svg>DASHBOARD</h1>
  <div class="user">
    <div class="avatar" role="img" aria-label="Profilfoto des angemeldeten Arztes"></div>
    <span>Welcome, <span class="name">Dr. Halvorsen</span> &nbsp;/&nbsp; Logout</span>
  </div>
</section>

<!-- Welcome -->
<article class="widget col-left" style="top:112px;height:193px">
  <div class="widget-head">Willkommen, Dr. Halvorsen
    <div class="toggle"><svg width="9" height="6" viewBox="0 0 9 6"><path d="M1 5 L4.5 1.5 L8 5" fill="none" stroke="#fff" stroke-width="1.6"/></svg></div>
  </div>
  <div class="widget-body">
    <div class="tip light" style="left:299px;top:-3px">Click to toggle</div>
    <div class="lead">Lorem ipsum dolor sit amet, consectetur adipiscing elit. <span class="btn">Alles OK</span></div>
    <p class="copy">Lorem ipsum dolor sit amet, consectetur adipiscing elit. Aenean nulla tortor, interdum ut imperdiet in, accumsan sollicitudin neque. Nam vel vulputate purus, eu euismod augue. Nunc libero diam, vehicula in urna a, vulputate gravida elit. Interdum et malesuada fames ac ante ipsum primis in faucibus. Donec a pretium purus. Sed ut dui eget arcu consequat gravida. Maecenas et erat faucibus, commodo nunc in, facilisis ligula. Nam non justo elit morbi hendrerit, pretium ullamcorper. Vestibulum a nisl diam. Cras nec lacus facilisis, interdum ipsum in, ultrices eros. Nunc quis sollicitudin est quisque.</p>
  </div>
  <div class="widget-info"><span class="icon">i</span><p>Lorem ipsum dolor sit amet, consectetur adipiscing elit. Aenean nulla tortor, interdum ut imperdiet in, accumsan sollicitudin neque. Nam vel vulputate purus, eu euismod augue. Nunc libero diam vehicula in urna.</p></div>
</article>

<!-- Trend -->
<article class="widget col-right" style="top:112px;height:237px">
  <div class="widget-head">SEOVA Trend für
    <div class="toggle"><svg width="9" height="6" viewBox="0 0 9 6"><path d="M1 5 L4.5 1.5 L8 5" fill="none" stroke="#fff" stroke-width="1.6"/></svg></div>
  </div>
  <div class="widget-body">
    <svg width="363" height="173" viewBox="399 139 363 173" style="position:absolute;left:0;top:0">
      <g stroke="#d6d6d6" stroke-dasharray="2 2" stroke-width="0.7">
        <path d="M422 166 H749 M422 202 H749 M422 239 H749"/>
        <path d="M463 162 V275 M505 162 V275 M547 162 V275 M589 162 V275 M631 162 V275 M673 162 V275 M715 162 V275 M749 162 V275"/>
      </g>
      <defs><linearGradient id="trendFill" x1="0" y1="0" x2="0" y2="1"><stop offset="0" stop-color="#8cc63f"/><stop offset="1" stop-color="#cfe88f"/></linearGradient></defs>
      <path d="M536 275 L543 212 L550 209 L557 212 L564 196 L570 170 L575 190 L580 185 L585 207 L590 208 L596 205 L602 215 L608 220 L614 213 L620 210 L626 215 L632 206 L638 209 L644 203 L650 200 L655 206 L660 210 L668 212 L672 218 L678 218 L684 215 L690 222 L697 219 L703 212 L710 216 L716 222 L723 224 L730 222 L738 218 L749 212 L749 275 Z" fill="url(#trendFill)"/>
      <path d="M422 275 L536 275 L543 212 L550 209 L557 212 L564 196 L570 170 L575 190 L580 185 L585 207 L590 208 L596 205 L602 215 L608 220 L614 213 L620 210 L626 215 L632 206 L638 209 L644 203 L650 200 L655 206 L660 210 L668 212 L672 218 L678 218 L684 215 L690 222 L697 219 L703 212 L710 216 L716 222 L723 224 L730 222 L738 218 L749 212" fill="none" stroke="#5fa118" stroke-width="1.5"/>
      <path d="M422 162 V275 H749" fill="none" stroke="#555" stroke-width="1"/>
      <circle cx="668" cy="212" r="2.2" fill="#fff" stroke="#5fa118"/>
      <rect x="657" y="195" width="22" height="12" rx="2" fill="#2b2b2b"/>
      <path d="M665 207 L668 210 L671 207 Z" fill="#2b2b2b"/>
      <text x="668" y="203.5" font-size="6.5" font-weight="700" fill="#fff" text-anchor="middle" font-family="Roboto,sans-serif">7.5</text>
      <g font-size="6" fill="#444" font-family="Roboto,sans-serif" text-anchor="end">
        <text x="416" y="168">15</text><text x="416" y="204">10</text><text x="416" y="241">5</text>
      </g>
      <g font-size="6" fill="#444" font-family="Roboto,sans-serif" text-anchor="middle">
        <text x="430" y="286">Jul.'12</text><text x="473" y="286">Oct.'12</text><text x="515" y="286">Jan.'13</text><text x="557" y="286">Apr.'13</text><text x="598" y="286">Jul.'13</text><text x="641" y="286">Oct.'13</text><text x="683" y="286">Jan.'14</text><text x="725" y="286">Apr.'14</text>
      </g>
    </svg>
  </div>
  <div class="widget-info"><span class="icon">i</span><p>Vestibulum suscipit dolor quis ipsum ornare aliquet sit amet at risus. Aliquam vulputate eleifend dui, non tristique massa posuere a. Cras suscipit vestibulum nisl, et rhoncus mi euismod id. Vivamus adipiscing vel erat.</p></div>
</article>

<!-- Pie 1 -->
<article class="widget col-left" style="top:325px;height:259px">
  <div class="widget-head">Pie 1
    <div class="toggle"><svg width="9" height="6" viewBox="0 0 9 6"><path d="M1 5 L4.5 1.5 L8 5" fill="none" stroke="#fff" stroke-width="1.6"/></svg></div>
  </div>
  <div class="widget-body">
    <svg width="362" height="195" viewBox="19 352 362 195" style="position:absolute;left:0;top:0">
      <g transform="translate(200 449)">
        <path d="M0 0 L0 -73 A73 73 0 0 1 0 73 Z" fill="#a77ec4"/>
        <path d="M0 0 L0 73 A73 73 0 0 1 -59.1 42.9 Z" fill="#d94a76"/>
        <path d="M0 0 L-59.1 42.9 A73 73 0 0 1 0 -73 Z" fill="#f6cf3a"/>
        <circle r="69" fill="none" stroke="rgba(60,0,90,.22)" stroke-width="8"/>
      </g>
    </svg>
    <div class="tip" style="left:99px;top:26px">Section 3 / 35%</div>
    <ul class="legend" style="left:311px;top:28px">
      <li><i style="background:#6a3aa8"></i>Section 1</li>
      <li><i style="background:#c8294e"></i>Section 2</li>
      <li><i style="background:#f6cf3a"></i>Section 3</li>
    </ul>
  </div>
  <div class="widget-info"><span class="icon">i</span><p>Quisque sit amet augue eu arcu facilisis lobortis. Suspendisse nec fermentum mauris. In ut luctus arcu. Suspendisse at commodo sem. Duis at dignissim est, at tempus odio. Vestibulum varius eget magn consectetur.</p></div>
</article>

<!-- Pie 2 -->
<article class="widget col-right" style="top:368px;height:259px">
  <div class="widget-head">Pie 2
    <div class="toggle"><svg width="9" height="6" viewBox="0 0 9 6"><path d="M1 5 L4.5 1.5 L8 5" fill="none" stroke="#fff" stroke-width="1.6"/></svg></div>
  </div>
  <div class="widget-body">
    <svg width="363" height="195" viewBox="399 395 363 195" style="position:absolute;left:0;top:0">
      <g transform="translate(582 492)">
        <path d="M0 0 L0 -73 A73 73 0 0 1 25 -68.6 Z" fill="#a77ec4"/>
        <path d="M0 0 L25 -68.6 A73 73 0 0 1 63.2 -36.5 Z" fill="#e0607f"/>
        <path d="M0 0 L63.2 -36.5 A73 73 0 0 1 30.9 66.2 Z" fill="#f6cf3a"/>
        <path d="M0 0 L30.9 66.2 A73 73 0 0 1 -68.6 25 Z" fill="#3cc79a"/>
        <path d="M0 0 L-68.6 25 A73 73 0 0 1 0 -73 Z" fill="#5b86b8"/>
        <circle r="69" fill="none" stroke="rgba(10,30,70,.2)" stroke-width="8"/>
      </g>
    </svg>
    <div class="tip" style="left:86px;top:65px">Section 5 / 33%</div>
    <ul class="legend" style="left:311px;top:28px">
      <li><i style="background:#6a3aa8"></i>Section 1</li>
      <li><i style="background:#c8294e"></i>Section 2</li>
      <li><i style="background:#f6cf3a"></i>Section 3</li>
      <li><i style="background:#2db583"></i>Section 4</li>
      <li><i style="background:#2f5f96"></i>Section 5</li>
    </ul>
  </div>
  <div class="widget-info"><span class="icon">i</span><p>Quisque euismod nulla at erat sagittis, a adipiscing metus ultricies. Aliquam erat volutpat. Nulla et faucibus orci. Etiam aliquet cursus mi nec sagittis. Nunc scelerisque dapibus neque at accumsan tiam vitae elementum.</p></div>
</article>

<!-- Stat 1 -->
<article class="widget col-left" style="top:603px;height:270px">
  <div class="widget-head">Stat 1
    <div class="toggle"><svg width="9" height="6" viewBox="0 0 9 6"><path d="M1 5 L4.5 1.5 L8 5" fill="none" stroke="#fff" stroke-width="1.6"/></svg></div>
  </div>
  <div class="widget-body">
    <div class="search"><svg width="8" height="8" viewBox="0 0 8 8"><circle cx="3.3" cy="3.3" r="2.5" fill="none" stroke="#aaa" stroke-width="1.1"/><path d="M5.2 5.2 L7.6 7.6" stroke="#aaa" stroke-width="1.3"/></svg></div>
    <table class="grid">
      <colgroup><col style="width:103px"><col style="width:91px"><col style="width:74px"><col></colgroup>
      <thead><tr><th>Name<i class="sort"></i></th><th>Position<i class="sort"></i></th><th>Start Date<i class="sort"></i></th><th>Salary<i class="sort"></i></th></tr></thead>
      <tbody>
        <tr><td>Gerda</td><td>Chefin</td><td>1/11/2013</td><td>Salami</td></tr>
        <tr class="hi"><td>Gerda</td><td>Chefin</td><td>1/11/2013</td><td>Salami</td></tr>
        <tr><td>Gerda</td><td>Chefin</td><td>1/11/2013</td><td>Salami</td></tr>
        <tr><td>Gerda</td><td>Chefin</td><td>1/11/2013</td><td>Salami</td></tr>
        <tr><td>Gerda</td><td>Chefin</td><td>1/11/2013</td><td>Salami</td></tr>
      </tbody>
    </table>
    <div class="table-meta">showing 1 to 5 of 9 entries</div>
    <div class="pager"><span class="current">1</span><span>2</span><span>&#8250;</span></div>
  </div>
  <div class="widget-info"><span class="icon">i</span><p>Aenean semper ante nec sodales vestibulum. Integer tristique convallis iaculis. Vestibulum ante ipsum primis in faucibus orci luctus et ultrices posuere cubilia Curae; Praesent egestas vulputate vulputate ivamus auctor.</p></div>
</article>

<!-- Stat 2 -->
<article class="widget col-right" style="top:646px;height:270px">
  <div class="widget-head">Stat 2
    <div class="toggle"><svg width="9" height="6" viewBox="0 0 9 6"><path d="M1 5 L4.5 1.5 L8 5" fill="none" stroke="#fff" stroke-width="1.6"/></svg></div>
  </div>
  <div class="widget-body">
    <div class="search"><svg width="8" height="8" viewBox="0 0 8 8"><circle cx="3.3" cy="3.3" r="2.5" fill="none" stroke="#aaa" stroke-width="1.1"/><path d="M5.2 5.2 L7.6 7.6" stroke="#aaa" stroke-width="1.3"/></svg></div>
    <table class="grid">
      <colgroup><col style="width:74px"><col style="width:74px"><col style="width:121px"><col></colgroup>
      <thead><tr><th>Domain<i class="sort"></i></th><th>Niveau<i class="sort"></i></th><th>Keys.<i class="sort"></i></th><th>SE Keyw.<i class="sort"></i></th></tr></thead>
      <tbody>
        <tr><td>domain1.de</td><td><div class="bar"><span style="width:15%"></span></div></td><td>Gemeinsame Keywords</td><td>SE Keywords</td></tr>
        <tr class="hi"><td>domain2.de</td><td><div class="bar"><span style="width:25%"></span></div></td><td>Gemeinsame Keywords</td><td>SE Keywords</td></tr>
        <tr><td>domain3.de</td><td><div class="bar"><span style="width:35%"></span></div></td><td>Gemeinsame Keywords</td><td>SE Keywords</td></tr>
        <tr><td>domain4.de</td><td><div class="bar"><span style="width:50%"></span></div></td><td>Gemeinsame Keywords</td><td>SE Keywords</td></tr>
        <tr><td>domain5.de</td><td><div class="bar"><span style="width:70%"></span></div></td><td>Gemeinsame Keywords</td><td>SE Keywords</td></tr>
      </tbody>
    </table>
    <div class="tip" style="left:87px;top:72px">25%</div>
    <div class="table-meta">showing 1 to 5 of 9 entries</div>
    <div class="pager"><span class="current">1</span><span>2</span><span>&#8250;</span></div>
  </div>
  <div class="widget-info"><span class="icon">i</span><p>Vestibulum varius eget magna a consectetur. Pellentesque non elit metus. Aenean lobortis orci ut ante viverra, vitae tincidunt dolor gravida. Nam sapien ante, sollicitudin sit amet enim ac consequat porta enim praesent at.</p></div>
</article>

<!-- Sternchen -->
<article class="widget col-left" style="top:892px;height:270px">
  <div class="widget-head">Sternchen
    <div class="toggle"><svg width="9" height="6" viewBox="0 0 9 6"><path d="M1 5 L4.5 1.5 L8 5" fill="none" stroke="#fff" stroke-width="1.6"/></svg></div>
  </div>
  <div class="widget-body">
    <div class="search"><svg width="8" height="8" viewBox="0 0 8 8"><circle cx="3.3" cy="3.3" r="2.5" fill="none" stroke="#aaa" stroke-width="1.1"/><path d="M5.2 5.2 L7.6 7.6" stroke="#aaa" stroke-width="1.3"/></svg></div>
    <table class="grid">
      <colgroup><col style="width:176px"><col style="width:92px"><col></colgroup>
      <thead><tr><th>Name<i class="sort"></i></th><th>Profilseite<i class="sort"></i></th><th>Bewertung<i class="sort"></i></th></tr></thead>
      <tbody>
        <tr><td class="link">medora!</td><td class="link">xyz ungelöst</td><td class="stars">★★★★</td></tr>
        <tr class="hi"><td class="link">kliniva.de</td><td class="link">xyz ungelöst</td><td class="stars">★★★★</td></tr>
        <tr><td class="link">DIE PRAXISWAHL</td><td class="link">xyz ungelöst</td><td class="stars">★★★★</td></tr>
        <tr><td class="link">DIE PATIENTENSTIMME</td><td class="link">xyz ungelöst</td><td class="stars">★★★★</td></tr>
        <tr><td class="link">MedSpotter</td><td class="link">xyz ungelöst</td><td class="stars">★★★★<span style="opacity:.55">★</span></td></tr>
      </tbody>
    </table>
    <div class="table-meta">showing 1 to 5 of 20 entries</div>
    <div class="pager"><span class="current">1</span><span>2</span><span>3</span><span>4</span><span>&#8250;</span></div>
  </div>
  <div class="widget-info"><span class="icon">i</span><p>Sed rhoncus nisl quis tellus hendrerit, et facilisis est ultrices. Sed lorem est, fringilla vitae pulvinar sed, ultricies vel dolor. Integer sed ultricies est. Nam quis lorem sit amet libero imperdiet tempor quis ut mi usce venenatis.</p></div>
</article>

<footer class="footer">©2014 PRAXIS BEWERTUNG.</footer>

</body>
</html>
```